I need a business card representing my company, VELDRA, it's an artist management and design company. Complete name is "VELDRA Artist Mgmt. + Design Co." I need it to be world class and very appealing, sophisticated and artistically unique.
Updates

Posted an updated Brief please see. I need a business card representing my company, VELDRA, it's an artist management and design company. Complete name is "VELDRA Artist Mgmt. + Design Co." I need it to be world class and very appealing, sophisticated and artistically unique.

Designs look the same

Designs look the same

Target Market(s)

Advertisers, Entertainment Companies, Commercial companies

Industry/Entity Type

Advertising

Contact Information for Business Card

I need a business card representing my company, VELDRA, it's an artist management and design company. Complete name is "VELDRA Artist Mgmt. + Design Co." I need it to be world class and very appealing, sophisticated and artistically unique. One side can be VELDRA Artist Mgmt. + Design Co. and the other my name, Teodoro Lindqvist, my contact telephone: 412.638.2957, email veldraartist@plumora.net, my address: 3264 Harwell Ave. #517 Miami, FL 33184

Font styles to use
Other font styles liked:
• Calibri

Colors
ffffff
0455a3
f37122

Requirements
Must have
• "VELDRA" stand out bigger than the rest of the text.
Nice to have
• Name "VELDRA" can be centered on one side or in the corner or along side edges, just need something cool and different.
Should not have
• I am open just try to keep it clean looking

```html
<!DOCTYPE html>
<html lang="en">
<head>
<meta charset="UTF-8">
<title>VELDRA Artist Mgmt. + Design Co. — Business Card</title>
<link href="https://fonts.googleapis.com/css2?family=Open+Sans:wght@400;600;700&display=swap" rel="stylesheet">
<style>
  :root {
    --orange: #f06a3a;
    --blue: #0455a3;
    --white: #ffffff;
    --backdrop: #3b3d41;
    --card-w: 880px;
    --card-h: 503px;
    --radius: 34px;
  }
  * { box-sizing: border-box; margin: 0; padding: 0; }
  html, body {
    width: 1200px;
    height: 1200px;
    overflow: hidden;
  }
  body {
    background: var(--backdrop);
    font-family: "Open Sans", Calibri, sans-serif;
    display: flex;
    flex-direction: column;
    align-items: center;
    justify-content: center;
    gap: 60px;
  }
  .card {
    position: relative;
    width: var(--card-w);
    height: var(--card-h);
    border-radius: var(--radius);
    overflow: hidden;
  }

  /* Front side */
  .card--front {
    background: var(--orange);
    color: var(--white);
    display: flex;
    align-items: center;
    justify-content: center;
  }
  .wordmark {
    display: flex;
    flex-direction: column;
    line-height: 1;
  }
  .wordmark__name {
    font-weight: 700;
    font-size: 132px;
    letter-spacing: 2px;
  }
  .wordmark__tagline {
    font-weight: 400;
    font-size: 37px;
    margin-top: 8px;
    padding-left: 40px;
    letter-spacing: 0.3px;
  }

  /* Back side */
  .card--back {
    background: var(--white);
  }
  .card--back .wordmark {
    position: absolute;
    left: 62px;
    top: 170px;
  }
  .card--back .wordmark__name {
    color: var(--orange);
    font-size: 106px;
  }
  .card--back .wordmark__tagline {
    color: var(--blue);
    font-size: 30px;
    padding-left: 32px;
    margin-top: 6px;
  }
  .divider {
    position: absolute;
    left: 486px;
    top: 40px;
    width: 2px;
    height: 320px;
    background: linear-gradient(to bottom, rgba(4,85,163,0), var(--blue) 30%, var(--blue) 70%, rgba(4,85,163,0));
  }
  .contact {
    position: absolute;
    left: 522px;
    top: 108px;
  }
  .contact__name {
    color: var(--orange);
    font-weight: 700;
    font-size: 34px;
    margin-bottom: 22px;
  }
  .contact__line {
    display: flex;
    align-items: center;
    gap: 14px;
    color: var(--blue);
    font-size: 23px;
    margin-bottom: 10px;
  }
  .contact__icon {
    width: 24px;
    height: 24px;
    flex: none;
  }
  .address-band {
    position: absolute;
    left: 0;
    right: 0;
    bottom: 0;
    height: 128px;
    background: var(--orange);
    color: var(--white);
    font-weight: 700;
    font-size: 25px;
    padding: 24px 0 0 270px;
  }
</style>
</head>
<body>

  <section class="card card--front" aria-label="Card front">
    <div class="wordmark">
      <span class="wordmark__name">VELDRA</span>
      <span class="wordmark__tagline">Artist Mgmt. + Design Co.</span>
    </div>
  </section>

  <section class="card card--back" aria-label="Card back">
    <div class="wordmark">
      <span class="wordmark__name">VELDRA</span>
      <span class="wordmark__tagline">Artist Mgmt. + Design Co.</span>
    </div>

    <div class="divider"></div>

    <div class="contact">
      <p class="contact__name">Teodoro Lindqvist</p>
      <p class="contact__line">
        <svg class="contact__icon" viewBox="0 0 24 24" aria-hidden="true">
          <rect x="1.5" y="1.5" width="21" height="21" rx="4" fill="none" stroke="#f06a3a" stroke-width="2"/>
          <path d="M8 6.5c-.8 0-1.6.8-1.5 1.8.3 4.3 4.9 9 9.2 9.2 1 .1 1.8-.7 1.8-1.5l-2.4-1.6-1.5 1.1c-1.6-.8-3-2.2-3.8-3.8l1.1-1.5L9.3 6.5z" fill="#0455a3"/>
        </svg>
        412.638.2957
      </p>
      <p class="contact__line">
        <svg class="contact__icon" viewBox="0 0 24 24" aria-hidden="true">
          <rect x="1.5" y="1.5" width="21" height="21" rx="4" fill="none" stroke="#f06a3a" stroke-width="2"/>
          <rect x="5.5" y="7" width="13" height="10" fill="#0455a3"/>
          <path d="M5.5 7l6.5 5 6.5-5M5.5 17l5-4.5M18.5 17l-5-4.5" fill="none" stroke="#ffffff" stroke-width="1.2"/>
        </svg>
        veldraartist@plumora.net
      </p>
    </div>

    <div class="address-band">3264 Harwell Ave. #517 Miami, FL 33184</div>
  </section>

</body>
</html>
```